Create Lanternfield HR Business Cards.

Create Business Cards for Lanternfield HR. 2 sided and Would like the back to have the logo.

Info for Business Card:
Address: 4827 Millbrook Ave Suite 230 Cleveland, Ohio 44987
Office Number: 216-555-0143
Mobile: 216-555-0192

Website: www.lanternfieldhr.example

Target Market(s)

Small to medium size businesses

Industry/Entity Type

Human Resources

Contact Information for Business Card

Company logo and information

Font styles to use
Serif
Sans Serif

Requirements
Must have
• Info for Business Card: Address: 4827 Millbrook Ave Suite 230 Cleveland, Ohio 44987 Office Number: 216-555-0143 Mobile: 216-555-0192 Website: www.lanternfieldhr.example

```html
<!DOCTYPE html>
<html lang="en">
<head>
<meta charset="utf-8">
<title>Lanternfield HR Business Cards</title>
<link href="https://fonts.googleapis.com/css2?family=Montserrat:wght@400;700;800&display=swap" rel="stylesheet">
<style>
  :root {
    --navy: #262160;
    --orange: #f58220;
    --white: #ffffff;
    --ink: #1c1c1c;
    --backdrop: #9e9e9e;
  }
  * { margin: 0; padding: 0; box-sizing: border-box; }
  html, body { width: 1159px; height: 1200px; overflow: hidden; }
  body {
    background: var(--backdrop);
    font-family: "Montserrat", Arial, sans-serif;
    position: relative;
  }
  .card {
    position: absolute;
    border-radius: 30px;
    overflow: hidden;
  }
  .brand-name {
    font-weight: 800;
    letter-spacing: 0.02em;
    text-transform: uppercase;
    white-space: nowrap;
    line-height: 1;
  }

  .card-front {
    left: 208px; top: 144px; width: 760px; height: 434px;
    background: var(--navy);
    display: flex; align-items: center; justify-content: center;
  }
  .card-front .brand-name { color: var(--white); font-size: 48px; }

  .card-back {
    left: 208px; top: 625px; width: 781px; height: 446px;
    background: var(--white);
  }
  .back-brand {
    position: absolute; right: 37px; top: 112px;
    color: var(--navy); font-size: 30px;
  }

  .holder { position: absolute; left: 43px; top: 226px; }
  .holder-name {
    font-weight: 700; font-size: 36px; color: var(--navy);
    letter-spacing: 0.01em; line-height: 1;
  }
  .holder-title {
    margin-top: 13px; font-weight: 400; font-size: 22px; color: var(--ink);
    letter-spacing: 0.03em; line-height: 1;
  }
  .divider {
    position: absolute; left: 43px; top: 298px; width: 700px; height: 1.5px;
    background: var(--ink);
  }
  .contact-list { position: absolute; left: 38px; top: 312px; list-style: none; }
  .contact-item {
    display: flex; align-items: center; gap: 12px;
    font-size: 21px; color: var(--ink); height: 33px;
  }
  .contact-item svg { width: 22px; height: 22px; flex: none; }
  .address {
    position: absolute; right: 37px; top: 334px;
    text-align: right; font-size: 21px; color: var(--ink); line-height: 30px;
    font-style: normal;
  }
  .base-bands { position: absolute; left: 0; bottom: 0; width: 781px; height: 18px; }
</style>
</head>
<body>
  <section class="card card-front" aria-label="Card front">
    <span class="brand-name">Lanternfield HR</span>
  </section>

  <section class="card card-back" aria-label="Card back">
    <span class="brand-name back-brand">Lanternfield HR</span>

    <div class="holder">
      <h1 class="holder-name">DANIEL REYES</h1>
      <p class="holder-title">MANAGING DIRECTOR</p>
    </div>
    <div class="divider"></div>

    <ul class="contact-list">
      <li class="contact-item">
        <svg viewBox="0 0 24 24" aria-hidden="true"><path fill="var(--orange)" d="M2 9c0-3 5-5 10-5s10 2 10 5v2h-5V8.5c-1.5-.6-3.2-.9-5-.9s-3.5.3-5 .9V11H2zM6 11l2-2h8l2 2 2 9H4z"/><circle cx="12" cy="15" r="2.2" fill="var(--white)"/></svg>
        216-555-0143
      </li>
      <li class="contact-item">
        <svg viewBox="0 0 24 24" aria-hidden="true"><rect x="6" y="2" width="12" height="20" rx="2" fill="none" stroke="var(--orange)" stroke-width="2.2"/><circle cx="12" cy="18.5" r="1.1" fill="var(--orange)"/></svg>
        216-555-0192
      </li>
      <li class="contact-item">
        <svg viewBox="0 0 24 24" aria-hidden="true"><g fill="none" stroke="var(--orange)" stroke-width="1.8"><circle cx="12" cy="12" r="9.5"/><ellipse cx="12" cy="12" rx="4.2" ry="9.5"/><path d="M2.5 12h19M4 7h16M4 17h16"/></g></svg>
        www.lanternfieldhr.example
      </li>
    </ul>

    <address class="address">
      4827 Millbrook Ave Suite 230<br>
      Cleveland, Ohio 44987
    </address>

    <svg class="base-bands" viewBox="0 0 781 18" preserveAspectRatio="none" aria-hidden="true">
      <polygon points="0,0 398,0 371,18 0,18" fill="var(--navy)"/>
      <polygon points="410,0 781,0 781,18 383,18" fill="var(--orange)"/>
    </svg>
  </section>
</body>
</html>
```